Employees at T&M Gale Power Solutions need new modern business cards

We need new business cards that showcase our new rebranded logo. We are seeking modern, clean, fresh, attractive cards while still being professional. We want to stand out. A little bit about us: we work in Canada and the USA. We offer Technical Field Advisors to support wind turbine manufacturers through the construction phase of wind farms. I am attaching a mock inspiration picture to lead you in the direction we want to see this go. Also, FYI We have approx. 10/11 different employees that would need their own card. Let me know when you would need everyone's name. We would love to see some black and white options as well as color copies- when using colors we want green to be the dominant color with accents for blue and orange (colors should match our logo). I have also attached copies of our old business card for reference.

Contact Information for Business Card

Name, Telephone, Email, address, company name, website. EXAMPLE: Hugh Marlow, HughMarlow@tandmgale.example, 555-381-4926, 217763 Birch Line #9, Elmhurst, ON X1Y 2Z3, www.tandmgale.example

Colors
0054AA
0677BA
7BADD7
CADEEF
E8F1F8
00AB8E
00BBA5
67D7C9
C6EFE9
E9F9F6
F0912C
F2A743
F7CA91
FBE8D2
FDF5EE

Requirements
Must have
• 2 sided business card

```html
<!DOCTYPE html>
<html lang="en">
<head>
<meta charset="utf-8">
<title>T&amp;M Gale Power Solutions – Business Card</title>
<link rel="stylesheet" href="https://fonts.googleapis.com/css2?family=Open+Sans:wght@300;400;600;700&display=swap">
<style>
  :root {
    --backdrop: #ababab;
    --card: #ffffff;
    --green: #2bb24c;
    --teal: #00ab8e;
    --blue: #0677ba;
    --blue-light: #7badd7;
    --orange: #f0912c;
    --amber: #f2a743;
    --ink: #111111;
    --muted: #777777;
    --rule: #9a9a9a;
  }
  * { box-sizing: border-box; margin: 0; padding: 0; }
  html, body { width: 1200px; height: 1000px; overflow: hidden; }
  body {
    background: var(--backdrop);
    font-family: "Open Sans", sans-serif;
    position: relative;
  }
  .card {
    position: absolute;
    left: 294px;
    width: 613px;
    height: 352px;
    border-radius: 22px;
    background: var(--card);
    overflow: hidden;
  }
  .card--front { top: 118px; }
  .card--back { top: 532px; }

  .front-decoration {
    position: absolute;
    left: 0; top: 0;
    width: 300px; height: 352px;
    background:
      radial-gradient(circle at 25% 20%, rgba(247,202,145,.45), transparent 45%),
      radial-gradient(circle at 70% 45%, rgba(198,239,233,.55), transparent 50%),
      radial-gradient(circle at 20% 85%, rgba(123,173,215,.35), transparent 50%);
  }

  .brand {
    position: absolute;
    display: flex;
    align-items: center;
    gap: 10px;
  }
  .brand__dot {
    width: 34px; height: 34px;
    border-radius: 50%;
    background: var(--green);
    flex: none;
  }
  .brand__name {
    color: var(--green);
    font-weight: 700;
    letter-spacing: 1px;
    line-height: 1.1;
    text-transform: uppercase;
  }
  .card--front .brand { left: 330px; top: 152px; }
  .card--front .brand__name { font-size: 19px; }
  .card--back .brand { left: 0; right: 0; top: 52px; justify-content: center; }
  .card--back .brand__name { font-size: 19px; }

  .back-glow {
    position: absolute;
    left: 0; right: 0; bottom: 0;
    height: 200px;
    background:
      radial-gradient(ellipse 42% 70% at 10% 100%, rgba(224,190,90,.95), transparent 75%),
      radial-gradient(ellipse 40% 70% at 48% 100%, rgba(40,120,150,.9), transparent 75%),
      radial-gradient(ellipse 45% 75% at 85% 100%, rgba(0,171,142,.9), transparent 75%),
      linear-gradient(to bottom, rgba(255,255,255,0), rgba(230,240,235,.3));
  }

  .person {
    position: absolute;
    right: 335px;
    top: 170px;
    text-align: right;
  }
  .person__name { font-size: 23px; color: var(--ink); font-weight: 400; line-height: 1.3; }
  .person__role { font-size: 20px; color: var(--amber); font-weight: 400; line-height: 1.45; }

  .divider {
    position: absolute;
    left: 306px; top: 168px;
    width: 2px; height: 71px;
    background: var(--rule);
  }

  .contacts {
    position: absolute;
    left: 326px; top: 166px;
    list-style: none;
  }
  .contacts li {
    display: flex; align-items: center; gap: 8px;
    height: 26px;
    font-size: 16px; font-weight: 300; color: var(--muted);
  }
  .contacts svg { width: 13px; height: 13px; flex: none; }

  .address {
    position: absolute;
    left: 0; right: 0; top: 314px;
    text-align: center;
    font-size: 13px; font-weight: 600; color: #ffffff;
    display: flex; justify-content: center; align-items: center; gap: 4px;
  }
  .address svg { width: 10px; height: 13px; }
</style>
</head>
<body>

<section class="card card--front">
  <div class="front-decoration" role="img" aria-label="Faint pastel brand decoration"></div>
  <div class="brand">
    <span class="brand__dot"></span>
    <span class="brand__name">T&amp;M Gale Power<br>Solutions</span>
  </div>
</section>

<section class="card card--back">
  <div class="back-glow"></div>
  <div class="brand">
    <span class="brand__dot"></span>
    <span class="brand__name">T&amp;M Gale Power<br>Solutions</span>
  </div>

  <div class="person">
    <p class="person__name">Hugh Marlow</p>
    <p class="person__role">Owner</p>
  </div>

  <div class="divider"></div>

  <ul class="contacts">
    <li>
      <svg viewBox="0 0 16 16" aria-hidden="true"><path fill="#0677ba" d="M3.6 1.5l2.3 2.8-1.3 1.6c.9 2 2.5 3.6 4.5 4.5l1.6-1.3 2.8 2.3-1.5 2.1C6.8 13.2 2.8 9.2 1.5 3z"/></svg>
      555-381-4926
    </li>
    <li>
      <svg viewBox="0 0 16 16" aria-hidden="true"><rect x="1" y="3" width="14" height="10" fill="#f2a743"/><path d="M1 3l7 5.5L15 3" fill="none" stroke="#fff" stroke-width="1.4"/></svg>
      hughmarlow@tandmgale.example
    </li>
    <li>
      <svg viewBox="0 0 16 16" aria-hidden="true"><circle cx="8" cy="8" r="7" fill="#2bb24c"/><path d="M1 8h14M8 1c-3 3-3 11 0 14M8 1c3 3 3 11 0 14" fill="none" stroke="#fff" stroke-width="1"/></svg>
      www.tandmgale.example
    </li>
  </ul>

  <p class="address">
    <svg viewBox="0 0 10 14" aria-hidden="true"><path fill="#fff" d="M5 0a5 5 0 0 0-5 5c0 3.5 5 9 5 9s5-5.5 5-9a5 5 0 0 0-5-5zm0 7a2 2 0 1 1 0-4 2 2 0 0 1 0 4z"/></svg>
    217763 Birch Line #9, Elmhurst, ON X1Y 2Z3
  </p>
</section>

</body>
</html>
```